Bref créative
Veloran Lending Group
Mortgage Lender
Professional
Gustav Kolbe
President
318 Birchwell Avenue
Regina, SK, S2K 8P4
Ph (306) 555-0142
Cl (306) 555-0187
Fx (306) 555-0143
gustav@veloran.ca
www.veloran.ca

```html
<!DOCTYPE html>
<html lang="en">
<head>
<meta charset="utf-8">
<title>Veloran Lending Group — Stationery</title>
<link href="https://fonts.googleapis.com/css2?family=Montserrat:wght@400;600;700&family=Great+Vibes&display=swap" rel="stylesheet">
<style>
  :root {
    --red: #e1262d;
    --ink: #1b1b1d;
    --ink-soft: #2c2c30;
    --grey: #7a7a7e;
    --paper: #ffffff;
    --bg: #e6e6e8;
  }
  * { box-sizing: border-box; margin: 0; padding: 0; }
  html, body { width: 1200px; height: 1067px; overflow: hidden; }
  body {
    position: relative;
    background: var(--bg);
    font-family: "Montserrat", Arial, sans-serif;
    color: var(--ink);
  }
  .sheet { position: absolute; background: var(--paper); box-shadow: 0 6px 18px rgba(0,0,0,.18); overflow: hidden; }

  .brand {
    display: flex; align-items: center; gap: 8px;
    font-weight: 700; letter-spacing: 2px; text-transform: uppercase; color: var(--ink);
  }
  .brand-square { width: 12px; height: 12px; background: var(--red); flex: none; }
  .brand--light { color: #ffffff; }

  /* Letterhead */
  .letterhead { left: 40px; top: 40px; width: 520px; height: 673px; padding: 40px 48px; }
  .letterhead .brand { justify-content: center; font-size: 19px; }
  .letter-body { margin-top: 38px; font-size: 8.6px; line-height: 1.6; color: #3a3a3d; }
  .letter-body p { margin-bottom: 10px; }
  .letter-date { margin-bottom: 4px; }
  .letter-salutation { font-weight: 600; }
  .signature { font-family: "Great Vibes", cursive; font-size: 28px; color: var(--ink); margin-top: -4px; }
  .letter-footer {
    position: absolute; left: 48px; right: 48px; bottom: 30px;
    border-top: 2px solid var(--red); padding-top: 8px;
    display: flex; justify-content: space-between; font-size: 8px; line-height: 1.6; color: var(--grey);
  }
  .letter-footer .web { color: var(--red); font-weight: 600; }

  /* Envelope */
  .envelope-flap { position: absolute; left: 620px; top: 180px; width: 540px; height: 130px; }
  .envelope { left: 620px; top: 300px; width: 540px; height: 250px; }
  .envelope .brand { position: absolute; left: 36px; top: 70px; font-size: 17px; }
  .envelope-window {
    position: absolute; left: 220px; top: 140px; width: 170px; height: 48px;
    border: 1px solid #cfcfd2; border-radius: 4px; background: #f6f6f7;
  }
  .envelope-return { position: absolute; left: 36px; bottom: 22px; font-size: 7.5px; line-height: 1.6; color: var(--grey); }
  .corner { position: absolute; }

  /* Business cards */
  .card { top: 790px; width: 380px; height: 217px; }
  .card-front { left: 40px; }
  .card-front .brand { position: absolute; left: 28px; top: 38px; font-size: 15px; }
  .card-band {
    position: absolute; left: 0; right: 0; bottom: 0; height: 112px; background: var(--ink);
    display: flex; justify-content: space-between; padding: 18px 28px;
    font-size: 8.5px; line-height: 1.7; color: #d6d6d8;
  }
  .card-person { text-align: right; padding-top: 18px; }
  .card-name { color: var(--red); font-weight: 700; font-size: 12px; }
  .card-title { color: #ffffff; font-size: 8.5px; letter-spacing: 1px; }
  .card-web { color: var(--red); font-weight: 600; }
  .card-back { left: 460px; background: var(--ink); }
  .card-back .brand { position: absolute; left: 0; right: 0; top: 92px; justify-content: center; font-size: 15px; }
  .card-back .card-web { position: absolute; left: 0; right: 0; top: 122px; text-align: center; font-size: 9px; }
</style>
</head>
<body>

  <article class="sheet letterhead">
    <div class="brand"><span class="brand-square"></span>Veloran Lending Group</div>
    <div class="letter-body">
      <p class="letter-date">12 March 2025</p>
      <p class="letter-salutation">Dear Mr. Owen Hale,</p>
      <p>Thank you for choosing us for your home financing needs. Our team has reviewed your application and we are pleased to confirm that your mortgage request has been approved under the terms we discussed during our recent meeting at the branch office.</p>
      <p>Enclosed you will find a summary of the rate, the amortization period and the payment schedule. Please read each page with care and contact your advisor if any detail needs to be changed before signing.</p>
      <p>Once the signed documents reach our office, funds will be released to your lawyer within five business days. We will keep you informed at every step so that your closing date stays on track.</p>
      <p>We appreciate your trust and look forward to serving you for many years to come.</p>
      <p>Yours Sincerely,</p>
      <p class="signature">Signature</p>
    </div>
    <footer class="letter-footer">
      <div>318 Birchwell Avenue<br>Regina, SK, S2K 8P4</div>
      <div>Ph (306) 555-0142<br>Fx (306) 555-0143</div>
      <div>gustav@veloran.ca<br><span class="web">www.veloran.ca</span></div>
    </footer>
  </article>

  <svg class="envelope-flap" viewBox="0 0 540 130" aria-hidden="true">
    <polygon points="0,130 270,0 540,130" fill="#1b1b1d"/>
  </svg>
  <article class="sheet envelope">
    <div class="brand"><span class="brand-square"></span>Veloran Lending Group</div>
    <div class="envelope-window"></div>
    <div class="envelope-return">318 Birchwell Avenue<br>Regina, SK, S2K 8P4</div>
    <svg class="corner" style="right:0;bottom:0" width="120" height="130" viewBox="0 0 120 130" aria-hidden="true">
      <polygon points="120,0 120,130 20,130" fill="#1b1b1d"/>
      <polygon points="120,30 120,130 55,130" fill="#e1262d"/>
    </svg>
  </article>

  <article class="sheet card card-front">
    <div class="brand"><span class="brand-square"></span>Veloran Lending Group</div>
    <svg class="corner" style="right:0;top:0" width="70" height="80" viewBox="0 0 70 80" aria-hidden="true">
      <polygon points="0,0 70,0 70,80" fill="#e1262d"/>
    </svg>
    <div class="card-band">
      <div>318 Birchwell Avenue<br>Regina, SK, S2K 8P4<br>Ph (306) 555-0142<br>Cl (306) 555-0187<br>gustav@veloran.ca</div>
      <div class="card-person">
        <div class="card-name">Gustav Kolbe</div>
        <div class="card-title">President</div>
        <div class="card-web">www.veloran.ca</div>
      </div>
    </div>
  </article>

  <article class="sheet card card-back">
    <div class="brand brand--light"><span class="brand-square"></span>Veloran Lending Group</div>
    <div class="card-web">www.veloran.ca</div>
    <svg class="corner" style="right:0;bottom:0" width="90" height="90" viewBox="0 0 90 90" aria-hidden="true">
      <polygon points="90,0 90,90 0,90" fill="#e1262d"/>
    </svg>
  </article>

</body>
</html>
```